Guess The Score (UK Football Predictions) Website and SM Graphic.

Hi guys, we're looking for a smart graphic to advertise our upcoming 'GUESS THE SCORE' competition on our new website. The design needs to be square and look contemporary. It needs to have a blank space for football team names and times to be inserted (please see attached image) and it needs to say that the prize will be a best-selling Terrace Verdict t-shirt. We've attached a rough digital design, but it needs to look much smarter than this. We don't just want a slightly better version of it - it needs to look radically different, and in a good way. Smart fonts, sharp graphics, compelling yet easy on the eye. It needs to feature our logo (we can supply this). The letter 'O' in SCORE needs to be a football (maybe). We're gonna leave it to you to knock us out.

Target Market(s)

Sports Fans, Sports Bettors, Football/Soccer Fans

Font styles to use
Sans Serif

Requirements
Must have
• Contemporary feel. Eye-catching.
Nice to have
• Maybe some animation.
Should not have
• Mustn't be boring.

```html
<!DOCTYPE html>
<html lang="en">
<head>
<meta charset="utf-8">
<title>Guess the Correct Score – Terrace Verdict</title>
<link rel="stylesheet" href="https://fonts.googleapis.com/css2?family=Oswald:wght@600&family=Poppins:wght@300;400;500;600&family=Saira+Condensed:wght@800&display=swap">
<style>
  :root {
    --bg-dark: #0b0b0b;
    --bg-mid: #161616;
    --green: #00f04c;
    --red: #ff1414;
    --white: #ffffff;
    --grey-icon: #5a5a5a;
    --photo-light: #9a9a9a;
    --photo-dark: #2a2a2a;
  }
  html, body {
    margin: 0;
    padding: 0;
    width: 1195px;
    height: 1200px;
    overflow: hidden;
    background: var(--bg-dark);
  }
  .poster {
    position: relative;
    width: 1195px;
    height: 1200px;
    overflow: hidden;
    background: radial-gradient(ellipse at 35% 40%, var(--bg-mid) 0%, var(--bg-dark) 70%);
    color: var(--white);
  }
  .poster-art {
    position: absolute;
    inset: 0;
    width: 1195px;
    height: 1200px;
  }
  .fixture-title {
    position: absolute;
    left: 29px;
    top: 68px;
    margin: 0;
    font: 600 76px/1 "Oswald", sans-serif;
    letter-spacing: 0;
    text-transform: uppercase;
  }
  .fixture-times {
    position: absolute;
    left: 30px;
    top: 151px;
    margin: 0;
    font: 300 41px/1.2 "Poppins", sans-serif;
  }
  .headline {
    position: absolute;
    left: 27px;
    margin: 0;
    font-family: "Saira Condensed", sans-serif;
    font-weight: 800;
    line-height: 1;
    text-transform: uppercase;
  }
  .headline--guess { top: 266px; font-size: 142px; color: var(--green); }
  .headline--correct { top: 384px; font-size: 194px; color: var(--green); letter-spacing: -2px; }
  .headline--score {
    top: 540px;
    font-size: 285px;
    color: var(--white);
    display: flex;
    align-items: center;
    gap: 0;
  }
  .score-ball {
    display: block;
    width: 206px;
    height: 206px;
    margin: 0 2px 0 6px;
  }
  .divider {
    position: absolute;
    left: 29px;
    top: 831px;
    width: 453px;
    height: 7px;
    background: var(--white);
  }
  .prize {
    position: absolute;
    left: 29px;
    top: 882px;
    margin: 0;
    font: 500 46px/1.43 "Poppins", sans-serif;
    text-transform: uppercase;
  }
  .prize-brand { color: var(--red); font-weight: 600; }
  .web-icon {
    position: absolute;
    left: 31px;
    top: 1055px;
    width: 74px;
    height: 74px;
  }
  .web-address {
    position: absolute;
    left: 29px;
    top: 1120px;
    margin: 0;
    font: 400 33px/1.2 "Poppins", sans-serif;
    letter-spacing: 3px;
  }
  .brand-mark {
    position: absolute;
    top: 112px;
    right: 28px;
    display: flex;
    align-items: center;
    gap: 12px;
  }
  .brand-dot {
    width: 40px;
    height: 40px;
    border-radius: 50%;
    background: var(--red);
  }
  .brand-name {
    font: 600 26px/1 "Poppins", sans-serif;
    color: var(--white);
    text-transform: uppercase;
  }
</style>
</head>
<body>
<main class="poster">
  <svg class="poster-art" viewBox="0 0 1195 1200" xmlns="http://www.w3.org/2000/svg">
    <defs>
      <linearGradient id="stadiumTone" x1="0" y1="0" x2="0.3" y2="1">
        <stop offset="0" stop-color="var(--photo-light)"/>
        <stop offset="0.45" stop-color="#555"/>
        <stop offset="1" stop-color="var(--photo-dark)"/>
      </linearGradient>
    </defs>
    <polygon class="stadium-photo" role="img" aria-label="Floodlit stadium in black and white with a footballer in a red kit volleying a ball"
      points="780,0 1195,0 1195,1200 806,1200 1092,746 1030,440" fill="url(#stadiumTone)"/>
    <polygon class="accent-band accent-band--red" points="688,0 780,0 1030,440 950,430" fill="var(--red)"/>
    <polygon class="accent-band accent-band--green" points="684,1200 806,1200 1092,746 1007,746" fill="var(--green)"/>
  </svg>

  <h2 class="fixture-title">Football Team Names</h2>
  <p class="fixture-times">TIMES TO BE INSERTED</p>

  <h1 class="headline headline--guess">Guess the</h1>
  <p class="headline headline--correct">Correct</p>
  <p class="headline headline--score" aria-label="Score">
    <span>SC</span>
    <svg class="score-ball" viewBox="0 0 206 206" role="img" aria-label="Football standing in for the letter O">
      <defs>
        <radialGradient id="ballTone" cx="0.4" cy="0.35" r="0.7">
          <stop offset="0" stop-color="#ffffff"/>
          <stop offset="0.7" stop-color="#d8d8d8"/>
          <stop offset="1" stop-color="#8a8a8a"/>
        </radialGradient>
      </defs>
      <circle cx="103" cy="103" r="101" fill="url(#ballTone)"/>
    </svg>
    <span>RE</span>
  </p>

  <div class="divider"></div>

  <p class="prize">And win a <span class="prize-brand">Terrace Verdict</span><br>T-Shirt!</p>

  <svg class="web-icon" viewBox="0 0 74 74" aria-hidden="true">
    <g fill="none" stroke="var(--grey-icon)" stroke-width="4">
      <circle cx="37" cy="37" r="34"/>
      <ellipse cx="37" cy="37" rx="15" ry="34"/>
      <line x1="37" y1="3" x2="37" y2="71"/>
      <line x1="3" y1="37" x2="71" y2="37"/>
      <line x1="9" y1="20" x2="65" y2="20"/>
      <line x1="9" y1="54" x2="65" y2="54"/>
    </g>
  </svg>
  <p class="web-address">www.website.com</p>

  <div class="brand-mark">
    <span class="brand-dot"></span>
    <span class="brand-name">Terrace Verdict</span>
  </div>
</main>
</body>
</html>
```